DJ company new brochure of services offered

I would like to get a new price sheet made for my company services. Currently it's text only. I would like to add pictures next to each service description also like to add general background colors, and just make it look more attractive overall.

Uplighting - File #4 & file #10
Centerpiece pin-spots - File #15
Wedding Cake Spot - file #13 (can you crop out the logo at the bottom)?
Dance Floor Decal File #5
Gobo Monogram - File # 3
market lighting - file #14
ballroom draping - file #7
Video/projections screens: File #13
Indoor safe sparkler effect (not listed on price sheet yet) File #11
Dancing on a cloud - File #9
Co2 Cannons - File #6

Target Market(s)

bride and grooms

Industry/Entity Type

Entertainment

Font styles to use
Serif

Colors

Designer to choose colors to be used in the design.

Requirements
Must have
• my website is www.brightloomevents.example
• instagram is: @brightloomevents.example

```html
<!DOCTYPE html>
<html lang="en">
<head>
<meta charset="utf-8">
<title>Additional Service Add-On Price Sheet</title>
<link href="https://fonts.googleapis.com/css2?family=Questrial&family=Nunito:wght@600;700&display=swap" rel="stylesheet">
<style>
  :root {
    --canvas: #ffffff;
    --page-dark: #141112;
    --panel: rgba(125, 118, 118, 0.32);
    --panel-edge: rgba(170, 160, 160, 0.55);
    --banner-red: #e30613;
    --tab-grey: #b9b6b6;
    --tab-ink: #1e1b1b;
    --text-light: #f4f1f1;
    --accent-red: #e0141c;
  }
  * { box-sizing: border-box; margin: 0; padding: 0; }
  html, body { width: 1200px; height: 1200px; overflow: hidden; background: var(--canvas); }
  body { font-family: "Questrial", sans-serif; color: var(--text-light); position: relative; }

  .sheet {
    position: absolute; left: 167px; top: 40px; width: 866px; height: 1120px;
    background: var(--page-dark);
  }
  .sheet-backdrop {
    position: absolute; inset: 0;
    background:
      radial-gradient(ellipse 45% 55% at 80% 40%, rgba(205,190,190,0.45), transparent 70%),
      radial-gradient(ellipse 60% 40% at 40% 20%, rgba(110,95,95,0.35), transparent 70%),
      linear-gradient(180deg, #2a2324 0%, #1a1516 70%, #0c0a0a 100%);
  }
  .banner {
    position: absolute; left: 43px; top: 58px; width: 780px; height: 44px;
    background: var(--banner-red); color: #fff;
    display: flex; align-items: center; justify-content: center;
    font-size: 20px; letter-spacing: 0.2px;
  }
  .banner small { font-size: 17px; margin-left: 6px; }
  .panel {
    position: absolute; left: 51px; top: 102px; width: 764px; height: 890px;
    background: var(--panel); border: 1px solid var(--panel-edge);
  }

  .photo { position: absolute; width: 169px; height: 129px; }
  .photo-wide { width: 170px; }

  .service { position: absolute; width: 173px; height: 129px; text-align: center; }
  .tab {
    height: 25px; background: var(--tab-grey); color: var(--tab-ink);
    font-size: 15px; line-height: 25px; margin-left: 10px;
  }
  .desc { font-size: 14px; line-height: 16px; margin-top: 15px; letter-spacing: 0.3px; }
  .price {
    font-family: "Nunito", sans-serif; font-weight: 700; font-size: 33px;
    position: absolute; left: 0; right: 0; bottom: 10px; letter-spacing: 0.5px;
  }
  .price sup { font-size: 18px; vertical-align: 14px; margin-right: 1px; }
  .price-large { font-size: 36px; bottom: 36px; }
  .per { position: absolute; left: 0; right: 0; bottom: 6px; font-size: 24px; font-family: "Nunito", sans-serif; font-weight: 600; }
  .desc-large { font-size: 21px; line-height: 24px; margin-top: 14px; letter-spacing: 0.8px; }

  .uplighting { position: absolute; left: 606px; top: 167px; width: 356px; height: 129px; }
  .uplighting .tab { margin-left: 0; }
  .tiers { display: flex; margin-top: 14px; }
  .tier { flex: 1; text-align: center; position: relative; height: 86px; }
  .tier + .tier { border-left: 1px solid var(--accent-red); }
  .tier .count { font-size: 15px; }
  .tier .room { font-size: 12px; margin-top: 3px; letter-spacing: 0.2px; }
  .tier .price { bottom: 0; }

  .footnote {
    position: absolute; left: 0; right: 0; top: 1052px; text-align: center;
    font-size: 14px; color: #e8e4e4;
  }
  .contacts {
    position: absolute; left: 217px; width: 766px; top: 1094px; height: 22px;
    display: flex; justify-content: space-between; align-items: center;
    font-family: "Nunito", sans-serif; font-weight: 600; font-size: 15px; color: var(--accent-red);
  }
  .contact { display: flex; align-items: center; gap: 5px; white-space: nowrap; }
  .contact svg { flex: none; }
</style>
</head>
<body>
<main class="sheet">
  <div class="sheet-backdrop" role="img" aria-label="Soft, dark photograph of a wedding couple in a ballroom"></div>
  <header class="banner">Additional Service Add-On <small>(When booked with DJ Package)</small></header>
  <div class="panel"></div>
</main>

<!-- Row 1 -->
<div class="photo" style="left:240px;top:167px;background:linear-gradient(160deg,#c99a6a,#6e4a30 55%,#2c1d16);" role="img" aria-label="Reception hall lit with warm amber uplighting"></div>
<div class="photo photo-wide" style="left:420px;top:167px;background:linear-gradient(170deg,#e7c8ef,#b57ad0 55%,#6e3b8a);" role="img" aria-label="Draped ballroom glowing in pink and violet uplighting"></div>
<section class="uplighting">
  <div class="tab">Room Up-lighting (color of your choice)</div>
  <div class="tiers">
    <div class="tier"><div class="count">20 fixtures</div><div class="room">(med-large room)</div><div class="price"><sup>$</sup>400</div></div>
    <div class="tier"><div class="count">16 fixtures</div><div class="room">(med-large room)</div><div class="price"><sup>$</sup>350</div></div>
    <div class="tier"><div class="count">12 fixtures</div><div class="room">(small-med room)</div><div class="price"><sup>$</sup>300</div></div>
  </div>
</section>

<!-- Row 2 -->
<div class="photo" style="left:240px;top:310px;background:linear-gradient(90deg,#4a2d6e,#2a1838 49%,#6b3f8a 51%,#c45a94);" role="img" aria-label="Before and after views of a floral centerpiece with pin spot lighting"></div>
<section class="service" style="left:420px;top:310px;">
  <div class="tab">Pin Spot Lighting</div>
  <div class="desc">centerpieces /<br>sweetheart table / etc.</div>
  <div class="price"><sup>$</sup>35+</div>
</section>
<div class="photo" style="left:606px;top:310px;background:radial-gradient(ellipse 40% 60% at 50% 55%,#f6eef6,#a35ec4 60%,#6c2d96);" role="img" aria-label="Tiered wedding cake under a soft spotlight against a purple backdrop"></div>
<section class="service" style="left:790px;top:310px;">
  <div class="tab">Cake Pin Spot</div>
  <div class="desc">soft spotlight on<br>wedding cake</div>
  <div class="price"><sup>$</sup>75</div>
</section>

<!-- Row 3 -->
<div class="photo" style="left:240px;top:453px;background:linear-gradient(180deg,#ece6dc,#c9b79c 55%,#f4f1ec);" role="img" aria-label="Couple dancing on a white floor with a custom name decal"></div>
<section class="service" style="left:420px;top:453px;">
  <div class="tab">Dance Floor Decal</div>
  <div class="desc">when booked with<br>dance floor</div>
  <div class="price"><sup>$</sup>400+</div>
</section>
<div class="photo" style="left:606px;top:453px;background:linear-gradient(175deg,#d7a8e6,#b96fd4 55%,#e6c7f0);" role="img" aria-label="Monogram projected onto a dance floor in a pink-lit ballroom"></div>
<section class="service" style="left:790px;top:453px;">
  <div class="tab">Gobo Monogram</div>
  <div class="desc">B&amp;G names/initals on<br>wall or dance floor</div>
  <div class="price"><sup>$</sup>250+</div>
</section>

<!-- Row 4 -->
<div class="photo" style="left:240px;top:596px;background:linear-gradient(150deg,#1a1630,#3a2a6a 50%,#8a2d24);" role="img" aria-label="Projection screen showing a slideshow in a dim event room"></div>
<section class="service" style="left:420px;top:596px;">
  <div class="tab">Video/Projection</div>
  <div class="desc">screens, projectors,<br>video display</div>
  <div class="price"><sup>$</sup>250+</div>
</section>
<div class="photo" style="left:606px;top:596px;background:linear-gradient(180deg,#3a3530,#8d7f6c 45%,#2b2622);" role="img" aria-label="Ballroom with draped walls and set dinner tables"></div>
<section class="service" style="left:790px;top:596px;">
  <div class="tab">Ballroom Draping</div>
  <div class="price price-large"><sup>$</sup>12 - <sup>$</sup>14</div>
  <div class="per">per ft.</div>
</section>

<!-- Row 5 -->
<div class="photo" style="left:240px;top:738px;background:linear-gradient(180deg,#1d2a40,#2f4c78 55%,#8fb0d6);" role="img" aria-label="Couple dancing amid low-lying fog on a dance floor"></div>
<section class="service" style="left:420px;top:738px;">
  <div class="tab">Dancing on a Cloud</div>
  <div class="desc">low-lying fog effect.<br>Indoor safe</div>
  <div class="price"><sup>$</sup>250</div>
</section>
<div class="photo" style="left:606px;top:738px;background:linear-gradient(180deg,#2d221c,#6a5646 50%,#d8d2cc);" role="img" aria-label="Couple embracing beside indoor sparkler fountains"></div>
<section class="service" style="left:790px;top:738px;">
  <div class="tab">Sparkler Effect</div>
  <div class="desc">indoor safe firework<br>simulator. no flame,<br>heat or smoke.</div>
  <div class="price" style="bottom:2px;"><sup>$</sup>175</div>
</section>

<!-- Row 6 -->
<div class="photo" style="left:240px;top:882px;background:linear-gradient(160deg,#e6dff0,#b9a7d2 50%,#5a3e62);" role="img" aria-label="Guests on a dance floor with CO2 cannon plumes"></div>
<section class="service" style="left:420px;top:882px;">
  <div class="tab">CO2 Cannon</div>
  <div class="desc">includes (2) CO2<br>cannons. stationary<br>jets also available.</div>
  <div class="price" style="bottom:2px;"><sup>$</sup>150</div>
</section>
<div class="photo" style="left:606px;top:882px;background:linear-gradient(180deg,#1c2030,#3c3a40 55%,#4a3a28);" role="img" aria-label="Outdoor dinner at dusk under strings of market lights"></div>
<section class="service" style="left:790px;top:882px;">
  <div class="tab">Market Lighting</div>
  <div class="desc desc-large">pricing<br>depends on<br>size and<br>area.</div>
</section>

<p class="footnote">* We offer a wide range of additional services. Please contact us for more info &amp; pricing.</p>

<footer class="contacts">
  <span class="contact">
    <svg width="18" height="18" viewBox="0 0 18 18" fill="none" stroke="#fff" stroke-width="1.3"><circle cx="9" cy="9" r="7.5"/><ellipse cx="9" cy="9" rx="3.2" ry="7.5"/><path d="M1.5 9h15M3 5h12M3 13h12"/></svg>
    www.brightloomevents.example
  </span>
  <span class="contact">
    <svg width="18" height="18" viewBox="0 0 24 24" fill="#fff"><path d="M6.6 10.8a15.2 15.2 0 0 0 6.6 6.6l2.2-2.2a1 1 0 0 1 1-.25 11.4 11.4 0 0 0 3.6.57 1 1 0 0 1 1 1V20a1 1 0 0 1-1 1A17 17 0 0 1 3 4a1 1 0 0 1 1-1h3.5a1 1 0 0 1 1 1c0 1.25.2 2.45.57 3.57a1 1 0 0 1-.25 1z"/></svg>
    555.010.4821
  </span>
  <span class="contact">
    <svg width="22" height="16" viewBox="0 0 22 16" fill="none" stroke="#fff" stroke-width="1.5"><rect x="1" y="1" width="20" height="14"/><path d="M1 1l10 8 10-8M1 15l7-6M21 15l-7-6"/></svg>
    hello@brightloomevents.example
  </span>
  <span class="contact">
    <svg width="18" height="18" viewBox="0 0 18 18"><rect x="1" y="1" width="16" height="16" fill="var(--accent-red)"/></svg>
    @brightloomevents
  </span>
</footer>
</body>
</html>
```